Torvane Partners Brochure Design

Design a brochure for Torvane Partners, with a focus on the three key areas of the business:
- Business Advisory (consulting);
- Turnaround;
- Business Valuations.

Details in relation to the above available at www.torvanepartners-example.com

The aim of the document is to have something which works in a digital and physical form. The brochure should have each of the above areas on a separate A4 page so as to enable them to be presented digitally as stand alone brochures. Alternative designs which achieve the same will be accepted, I.e. Multiple brochures, one for whole of business and one for each business area.

Should also have a brief bio on Peter Lindgrove and Torvane Partners, also on a separate page or included in separate brochures if this approach is taken.

Industry/Entity Type

Digital

Requirements
Must have
• Please ensure that design flows from website.

```html
<!DOCTYPE html>
<html lang="en">
<head>
<meta charset="utf-8">
<title>Torvane Partners Brochure</title>
<link href="https://fonts.googleapis.com/css2?family=Arimo:wght@400;700&display=swap" rel="stylesheet">
<style>
  :root {
    --bg: #4b4b4b;
    --paper: #ffffff;
    --brand-blue: #2f9fd0;
    --brand-blue-dark: #1f7fae;
    --accent-yellow: #f6c21a;
    --ink: #4a4f55;
    --ink-soft: #6d737a;
    --strip-dark: #1d2125;
  }
  * { box-sizing: border-box; margin: 0; padding: 0; }
  html, body { width: 1200px; height: 900px; overflow: hidden; }
  body {
    background: var(--bg);
    font-family: "Arimo", Arial, sans-serif;
    color: var(--ink);
    position: relative;
  }

  /* ---------- Inner spread ---------- */
  .spread {
    position: absolute; left: 50px; top: 30px;
    width: 1100px; height: 389px;
    display: flex;
  }
  .page { position: relative; width: 550px; height: 389px; background: var(--paper); overflow: hidden; }
  .photo-meeting {
    position: absolute; inset: 0;
    background: linear-gradient(135deg, #dfe8ef 0%, #8fa6bd 35%, #3d5674 65%, #1e2f47 100%);
  }
  .brand {
    position: absolute; display: flex; align-items: center; gap: 6px;
    font-weight: 700; color: var(--brand-blue); white-space: nowrap;
  }
  .brand-square { background: var(--brand-blue); display: block; }
  .page-right .brand { top: 20px; right: 26px; font-size: 11px; }
  .page-right .brand-square { width: 10px; height: 10px; }

  .service-title {
    position: absolute; left: 30px; top: 52px;
    font-size: 18px; font-weight: 400; color: var(--brand-blue);
  }
  .intro-band {
    position: absolute; left: 0; right: 0; top: 78px;
    background: var(--brand-blue); color: #fff;
    padding: 9px 30px 10px 30px;
    font-size: 8.6px; line-height: 1.45;
  }
  .columns {
    position: absolute; left: 30px; right: 30px; top: 150px;
    display: grid; grid-template-columns: 1fr 1fr; column-gap: 26px;
  }
  .columns h3 {
    font-size: 10px; font-weight: 400; color: var(--brand-blue);
    margin: 10px 0 4px;
  }
  .columns h3:first-child { margin-top: 0; }
  .columns p, .columns li { font-size: 6.6px; line-height: 1.5; color: var(--ink-soft); }
  .columns ul { margin: 4px 0 5px 10px; }

  /* ---------- Cover ---------- */
  .cover {
    position: absolute; left: 325px; top: 460px;
    width: 550px; height: 389px; overflow: hidden;
    background: var(--paper);
  }
  .photo-city {
    position: absolute; inset: 0;
    background: linear-gradient(180deg, #e9eef2 0%, #b9c3cc 25%, #8a97a3 55%, #5f6b77 85%, #454e58 100%);
  }
  .cover .brand { top: 34px; left: 28px; font-size: 15px; color: var(--brand-blue-dark); }
  .cover .brand-square { width: 14px; height: 14px; background: var(--brand-blue-dark); }
  .cover-band {
    position: absolute; left: 0; top: 143px; width: 400px;
    background: var(--brand-blue); padding: 6px 0 6px 26px; color: #fff;
  }
  .cover-headline { font-size: 29px; font-weight: 400; line-height: 1.05; }
  .cover-tagline { font-size: 15px; font-weight: 700; color: var(--accent-yellow); opacity: .95; }
  .cover-tagline strong { color: var(--accent-yellow); }
  .cover-tagline span { font-weight: 400; }
  .cover-strip {
    position: absolute; left: 0; right: 0; bottom: 0; height: 36px;
    background: var(--strip-dark);
    display: flex; align-items: center; justify-content: flex-end;
    padding-right: 18px;
  }
  .cover-url { color: #fff; font-size: 11px; font-weight: 700; }
</style>
</head>
<body>

<section class="spread">
  <div class="page page-left">
    <div class="photo-meeting" role="img" aria-label="Photograph of a businessman in a suit reviewing documents with a pen at a desk"></div>
  </div>
  <div class="page page-right">
    <div class="brand"><span class="brand-square"></span>Torvane Partners</div>
    <h2 class="service-title">Turnaround Advisors</h2>
    <p class="intro-band">Often external factors can result in a business being at risk of failure. In these situations Torvane Partners turnaround advisors are qualified to identify the critical issues faced by businesses and can provide assistance in resolving these issues, through expert business management, we access the position of the company and prepare a plan to move forward. This plan is likely to include some or all of the following processes:</p>
    <div class="columns">
      <div class="column">
        <h3>Negotiation with Tax Office and other Creditors</h3>
        <p>We can negotiate payment arrangements with creditors or the tax office, giving the business time to restore cash flow and trade on with confidence.</p>
        <h3>Cash flow management</h3>
        <p>We review the timing of payments and receipts and build a weekly forecast so that the owners can see where each dollar goes.</p>
        <h3>Finance and working capital</h3>
        <p>We help secure finance on fair terms and free working capital held in stock and debtors to support the plan.</p>
      </div>
      <div class="column">
        <h3>Solvency Support</h3>
        <p>Where the business faces serious financial stress we work with the directors to review all options available and act early.</p>
        <ul>
          <li>Informal creditor arrangements</li>
          <li>Voluntary administration</li>
          <li>Deed of company arrangement</li>
          <li>Restructure of debt</li>
        </ul>
        <p>For further guidance please contact our team to discuss how we can help your business recover and grow.</p>
      </div>
    </div>
  </div>
</section>

<section class="cover">
  <div class="photo-city" role="img" aria-label="Photograph of a businessman standing on a rooftop ledge looking out over a hazy city skyline"></div>
  <div class="brand"><span class="brand-square"></span>Torvane Partners</div>
  <div class="cover-band">
    <h1 class="cover-headline">Looking to the future</h1>
    <p class="cover-tagline"><span>Our passion is to see</span> <strong>you succeed</strong></p>
  </div>
  <div class="cover-strip"><span class="cover-url">www.torvanepartners-example.com</span></div>
</section>

</body>
</html>
```